Sunvale Ride Co Splashpage

This webpage will be a holding page until our website is complete. This page needs to be designed to advertise our tours in Honolulu, Hawaii. So it is important to have prices displayed and have a Hawaiian theme.

1. Warm colors - suggest reds?
2. Hawaiian flower incorporated in design

3. Display prices
Adult - single Journey - $20
Adult - 1 Day - $20 (this needs to be displayed as a special deal/price because full price is $25)
Adult - 2 days - $30

Seniors - (62+) 1 Day + 1 Day Free - $20

Children 5 - 17 yrs - 1 Day - $13
Children 5 - 17 yrs - 2 Days - $15
Under 5 Yrs - Free

There will be an online booking button (text on button should say "Book Online", so please make sure it is clear where they can purchase the tickets.

3. A photo of our branded double decker bus should be incorporate on the page.

4. Our Message "Welcome to Sunvale Ride Co. Our Open Top Bus ensures you have an unrivalled view of Honolulu and all that this great city has to offer. We pass all of the city’s main sites, offering fantastic photo opportunities along the way. Our tour takes around 90 minutes. You can get on and off the bus as often as you want. Your ticket is valid for one or two days. All departures have commentary in English. If it’s raining, we have a sliding roof to keep you dry. Step on-board and let us show you the best of Honolulu."

5. Some tour sites our tour visits are: Marlow's Arcade, Waikiki beach, Umerik Palace, Bretoma Palace/King statue, Darvin's statue

We are catering to an international adult audience (ranging from 25 - 60 yrs of age) that handles vacation planning.

Please visit www.ridebyloop.ee to get an idea of our style.

• 1. prices displayed where they be viewed easily - There will be an online booking button so please make sure it is clear where they can purchase the tickets.

2. Adult - 1 Day - $20 (this needs to be displayed as a special deal/price because full price is $25)

3. Photo of our double decker bus

4. Hawaiian flower incorporated in design

5. Bright colors (make sure orange isn't the main background color) but not overwhelming

6. Logo on webpage
• 1. Images of our tour sites
2. Other Hawaiian images such as palm trees, Maile Lei, Sun with sunglasses, flower lei, parrot, Hawaiian sunsets
• -Do not want any shade of orange as the main background color

```html
<!DOCTYPE html>
<html lang="en">
<head>
<meta charset="utf-8">
<title>Sunvale Ride Co</title>
<link rel="stylesheet" href="https://fonts.googleapis.com/css2?family=Source+Sans+3:ital,wght@0,400;0,600;0,700;1,400;1,600&display=swap">
<style>
  :root {
    --red: #e30b0b;
    --yellow: #fcf43a;
    --yellow-deep: #f7d705;
    --ink: #111111;
    --dark: #1f1a14;
    --footer: #000000;
    --white: #ffffff;
    --offer-red: #e5141b;
  }
  * { box-sizing: border-box; margin: 0; padding: 0; }
  html, body { width: 1200px; height: 934px; overflow: hidden; background: var(--dark); }
  .page { position: relative; width: 1200px; height: 934px; font-family: "Source Sans 3", Arial, sans-serif; }

  .hero-photo {
    position: absolute; left: 0; top: 0; width: 1200px; height: 476px;
    background:
      linear-gradient(180deg, rgba(210,220,225,.35) 0%, rgba(0,0,0,0) 30%, rgba(0,0,0,0) 68%, rgba(90,95,90,.55) 76%, rgba(80,130,50,.6) 100%),
      linear-gradient(90deg, #5f7a55 0%, #9aa58a 12%, #c9c3ad 19%, #d42a22 23%, #cf1f1b 50%, #c71c18 74%, #d9d0bb 80%, #cfc2a6 92%, #8a8a66 100%);
  }
  .brand {
    position: absolute; left: 78px; top: 24px;
    font-size: 48px; font-weight: 700; line-height: 56px; color: var(--yellow); letter-spacing: 1px;
  }

  .deal-band { position: absolute; left: 0; top: 476px; width: 1200px; height: 201px; background: var(--red); }

  .deal-card {
    position: absolute; top: 379px; width: 318px; height: 129px;
    background: linear-gradient(180deg, var(--yellow) 0%, #fbf02c 70%, var(--yellow-deep) 100%);
    border: 3px solid var(--yellow-deep); border-radius: 14px;
    box-shadow: 0 6px 10px rgba(120,0,0,.45);
    padding: 15px 0 0 30px; color: var(--ink);
  }
  .deal-card--adult { left: 74px; }
  .deal-card--seniors { left: 439px; }
  .deal-card--children { left: 794px; }
  .deal-title { font-size: 30px; font-weight: 600; line-height: 30px; }
  .deal-line { font-size: 18.5px; font-weight: 600; line-height: 20.5px; }
  .view-details {
    position: absolute; right: 36px; bottom: 9px;
    font-family: Arial, sans-serif; font-size: 12px; font-style: italic; color: var(--ink);
  }

  .welcome {
    position: absolute; left: 82px; top: 531px; width: 645px;
    font-family: Arial, sans-serif; font-size: 13px; font-weight: 700; font-style: italic;
    line-height: 17.3px; color: var(--white);
    text-shadow: 1px 1px 1px rgba(0,0,0,.5);
  }

  .special-offer {
    position: absolute; left: 794px; top: 524px; width: 318px; height: 130px;
    border-radius: 14px; border: 2px solid #f4f4f4;
    background: linear-gradient(180deg, #ffffff 0%, #e4e4e4 55%, #b9b9b9 100%);
    box-shadow: 0 6px 10px rgba(100,0,0,.5);
    text-align: center; padding-top: 4px;
  }
  .offer-label { font-size: 23px; font-style: italic; font-weight: 600; color: var(--ink); line-height: 27px; }
  .offer-price { font-size: 31px; font-weight: 700; color: var(--offer-red); line-height: 35px; }
  .offer-book { font-size: 23px; font-style: italic; font-weight: 600; color: var(--ink); line-height: 27px; }
  .offer-discount { font-size: 31px; font-weight: 700; color: var(--offer-red); line-height: 36px; }

  .gallery-band {
    position: absolute; left: 0; top: 677px; width: 1200px; height: 222px;
    background: repeating-linear-gradient(90deg, #231d16 0 2px, #1b1611 2px 4px);
  }
  .gallery-thumb {
    position: absolute; top: 703px; width: 190px; height: 167px;
    border: 3px solid var(--white);
  }
  .gallery-arrow { position: absolute; top: 774px; width: 40px; height: 40px; }

  .footer {
    position: absolute; left: 0; top: 899px; width: 1200px; height: 35px; background: var(--footer);
    color: var(--white); font-family: Arial, sans-serif; font-size: 12px; text-align: center; line-height: 35px;
  }
</style>
</head>
<body>
<div class="page">
  <div class="hero-photo" role="img" aria-label="Photo of the red open-top double decker tour bus on a palm-lined Honolulu street"></div>
  <div class="brand">Sunvale Ride Co</div>

  <div class="deal-band"></div>

  <div class="deal-card deal-card--adult">
    <h2 class="deal-title">Adult Deals</h2>
    <p class="deal-line">Adult - Single Journey - $20</p>
    <p class="deal-line">Adult - 2 days $30</p>
    <span class="view-details">View Details</span>
  </div>
  <div class="deal-card deal-card--seniors">
    <h2 class="deal-title">Seniors Deals</h2>
    <p class="deal-line">(62+) 1Day + 1 Day Free - $20</p>
    <span class="view-details">View Details</span>
  </div>
  <div class="deal-card deal-card--children">
    <h2 class="deal-title">Children Deals</h2>
    <p class="deal-line">Children 5 - 17 yrs - 1 Day - $13</p>
    <p class="deal-line">Children 5 - 17 yrs - 2 Days - $15</p>
    <p class="deal-line">Under 5 Yrs - Free</p>
    <span class="view-details">View Details</span>
  </div>

  <p class="welcome">Welcome to Sunvale Ride Co. Our Open Top Bus ensures you have an unrivalled view of Honolulu and all that this great city has to offer. We pass all of the city’s main sites, offering fantastic photo opportunities along the way. Our tour takes around 90 minutes. You can get on and off the bus as often as you want. Your ticket is valid for one or two days. All departures have commentary in English. If it’s raining, we have a sliding roof to keep you dry. Step on-board and let us show you the best of Honolulu.</p>

  <div class="special-offer">
    <p class="offer-label">Special Offer</p>
    <p class="offer-price">Adult - 1 Day - $20</p>
    <p class="offer-book">Book Online</p>
    <p class="offer-discount">10% Discount</p>
  </div>

  <div class="gallery-band"></div>
  <svg class="gallery-arrow" style="left:46px" viewBox="0 0 40 40" aria-label="Previous">
    <circle cx="20" cy="20" r="19" fill="#f8ec12"/>
    <path d="M23 12 L15 20 L23 28" fill="none" stroke="#111" stroke-width="4.5" stroke-linecap="round" stroke-linejoin="round"/>
  </svg>
  <div class="gallery-thumb" style="left:103px;background:linear-gradient(180deg,#eef0f2 0%,#d9d6cc 45%,#6b7f4e 100%)" role="img" aria-label="Photo of Umerik Palace with palm trees"></div>
  <div class="gallery-thumb" style="left:307px;background:linear-gradient(180deg,#f2f2f2 0%,#c8343a 30%,#f0ece4 55%,#3d6b3a 100%)" role="img" aria-label="Photo of Marlow's Arcade storefront"></div>
  <div class="gallery-thumb" style="left:511px;background:linear-gradient(180deg,#3b86d8 0%,#7fb0e0 40%,#8a5a2e 70%,#3f6a2c 100%)" role="img" aria-label="Photo of the bronze king statue with a surfboard near Waikiki beach"></div>
  <div class="gallery-thumb" style="left:715px;background:linear-gradient(180deg,#c56a58 0%,#f1a57c 45%,#e58a70 60%,#3a1f22 100%)" role="img" aria-label="Photo of a Hawaiian sunset with palm trees reflected in water"></div>
  <div class="gallery-thumb" style="left:916px;background:linear-gradient(180deg,#2f7ad6 0%,#9cc6ea 40%,#d8d2c2 55%,#1f8fc8 100%)" role="img" aria-label="Photo of Waikiki beach and the city skyline"></div>
  <svg class="gallery-arrow" style="left:1120px" viewBox="0 0 40 40" aria-label="Next">
    <circle cx="20" cy="20" r="19" fill="#f8ec12"/>
    <path d="M17 12 L25 20 L17 28" fill="none" stroke="#111" stroke-width="4.5" stroke-linecap="round" stroke-linejoin="round"/>
  </svg>

  <footer class="footer">Copyright © 2011 sunvaleride.com</footer>
</div>
</body>
</html>
```